Business Card Design Project

TRX Solutions is a Electrical and Communications Services and Maintenance contractor to the Mining Oil and Gas sectors of Australia.
Our clients will be planners, Schedulers, Tradespeople and Engineers

We are yet to determine the primary colours that we will use on the business cards but the logos attached will form foundation of the colours used for logos on Business cards, Website, Uniforms, vehicles etc.

Target Market(s)

Mining engineers and shedulers

Industry/Entity Type

Contractor

Requirements
Must have
• information to be included on the card

Name: Derek Hanley
Title: Managing Director
Company: TRX Solutions Pty Ltd
Phone: 08 9XXX XXXX
Mobile 0400 318 942
email: dhanley@trxsolutionsgroup.com.au
Website www.trxsolutionsgroup.com.au

Address: U5/14 Kettering Street Ashgrove Flats, WA 6071
Postal Address: PO Box 7183 Ashgrove Flats WA 6975

Nice to have
• Double sided. Maybe the logo on the back

```html
<!DOCTYPE html>
<html lang="en">
<head>
<meta charset="utf-8">
<title>TRX Solutions — Business Card</title>
<link rel="stylesheet" href="https://fonts.googleapis.com/css2?family=Arimo:wght@400;700&display=swap">
<style>
  :root {
    --backdrop: #1c1c1c;
    --card-white: #ffffff;
    --navy: #0f2446;
    --navy-light: #17325c;
    --swoosh-grey: #c9cbcf;
    --ink: #1e2a3c;
    --accent-red: #e3232c;
    --logo-navy: #13284a;
  }
  * { margin: 0; padding: 0; box-sizing: border-box; }
  html, body {
    width: 1200px;
    height: 900px;
    overflow: hidden;
    background: var(--backdrop);
    font-family: "Arimo", Arial, sans-serif;
  }
  .stage {
    position: relative;
    width: 1200px;
    height: 900px;
  }
  .card {
    position: absolute;
    top: 301px;
    width: 522px;
    height: 299px;
    overflow: hidden;
  }
  .card--front { left: 72px; background: var(--card-white); }
  .card--back {
    left: 616px;
    background: radial-gradient(ellipse at 50% 45%, var(--navy-light) 0%, var(--navy) 75%);
  }
  .front-swoosh {
    position: absolute;
    inset: 0;
    width: 522px;
    height: 299px;
  }
  .contact-block {
    position: absolute;
    left: 26px;
    top: 68px;
    color: var(--ink);
  }
  .person-name {
    font-size: 15px;
    font-weight: 700;
    line-height: 18px;
  }
  .person-title {
    font-size: 14px;
    line-height: 18px;
    margin-bottom: 24px;
  }
  .company-name {
    font-size: 12px;
    line-height: 16px;
    margin-left: 3px;
    margin-bottom: 4px;
  }
  .contact-list { list-style: none; }
  .contact-list li {
    display: flex;
    align-items: center;
    gap: 6px;
    font-size: 12px;
    line-height: 16.5px;
    margin-left: 3px;
  }
  .contact-icon { width: 10px; height: 10px; flex: none; }
  .address-block {
    margin-top: 4px;
    font-size: 12px;
    line-height: 16.5px;
    white-space: nowrap;
  }
  .brand-name {
    position: absolute;
    font-weight: 700;
    letter-spacing: 1px;
    white-space: nowrap;
  }
  .brand-name--front {
    right: 38px;
    top: 104px;
    font-size: 30px;
    color: var(--logo-navy);
  }
  .brand-name--back {
    left: 0;
    right: 0;
    top: 118px;
    text-align: center;
    font-size: 38px;
    color: var(--card-white);
  }
  .back-web {
    position: absolute;
    left: 0;
    right: 0;
    top: 267px;
    text-align: center;
    font-size: 11px;
    letter-spacing: 2.4px;
    color: #e6e9ef;
  }
</style>
</head>
<body>
<main class="stage">

  <section class="card card--front" aria-label="Business card front">
    <svg class="front-swoosh" viewBox="0 0 522 299" aria-hidden="true">
      <path d="M250 299 C 360 275, 460 248, 522 208 L 522 299 Z" fill="var(--swoosh-grey)"/>
      <path d="M290 299 C 390 282, 470 258, 522 226 L 522 299 Z" fill="var(--navy)"/>
      <path d="M330 299 C 420 288, 480 268, 522 244" fill="none" stroke="#0a1a33" stroke-width="3"/>
    </svg>

    <div class="contact-block">
      <p class="person-name">Derek Hanley</p>
      <p class="person-title">Managing Director</p>
      <p class="company-name">TRX Solutions Pty Ltd</p>
      <ul class="contact-list">
        <li>
          <svg class="contact-icon" viewBox="0 0 10 10"><path d="M1 1h4v8H1z M6 5h3v4H6z" fill="var(--accent-red)"/></svg>
          08 9XXX XXXX
        </li>
        <li>
          <svg class="contact-icon" viewBox="0 0 10 10"><rect x="2.5" y="0.5" width="5" height="9" rx="1" fill="none" stroke="var(--accent-red)" stroke-width="1.2"/></svg>
          0400 318 942
        </li>
        <li>
          <svg class="contact-icon" viewBox="0 0 10 10"><rect x="0.6" y="2" width="8.8" height="6" fill="none" stroke="var(--accent-red)" stroke-width="1.1"/><path d="M0.6 2 L5 5.6 L9.4 2" fill="none" stroke="var(--accent-red)" stroke-width="1.1"/></svg>
          dhanley@trxsolutionsgroup.com.au
        </li>
        <li>
          <svg class="contact-icon" viewBox="0 0 10 10"><circle cx="5" cy="5" r="4.5" fill="var(--accent-red)"/><path d="M0.5 5h9 M5 0.5c-2 2.5-2 6.5 0 9 M5 0.5c2 2.5 2 6.5 0 9" fill="none" stroke="#fff" stroke-width="0.7"/></svg>
          www.trxsolutionsgroup.com.au
        </li>
      </ul>
      <div class="address-block">
        <p>Address:</p>
        <p>U5/14 Kettering Street Ashgrove Flats, WA 6071</p>
        <p>Postal Address:</p>
        <p>PO Box 7183 Ashgrove Flats WA 6975</p>
      </div>
    </div>

    <p class="brand-name brand-name--front">TRX Solutions</p>
  </section>

  <section class="card card--back" aria-label="Business card back">
    <p class="brand-name brand-name--back">TRX Solutions</p>
    <p class="back-web">www.trxsolutionsgroup.com.au</p>
  </section>

</main>
</body>
</html>
```